Business card for my new company (Accounting firm)

I need a business card for my new business Quervane Advisory and Finance SA. Our services are accounting, tax, audit and financial management. Our customers are small companies, start-ups and new companies. The final design has to show financial security, trust and growth. Please find our logo attached to the business card. Text for the business card: Quervane Advisory and Finance SA Tomas de Valbueno Director and Founder Certified Accountant Tel. 022 418 27 53 tv@quervane-conseil.ch www.quervane-conseil.ch Rue des Verniquets 14 1201 Geneva
Target Market(s)
Our customers are small companies, start-ups and new companies.
Industry/Entity Type
Finance And Accounting
Contact Information for Business Card
Quervane Conseil et Finance SA
Tomas de Valbueno
Directeur et Fondateur
Expert-comptable diplômé
Tél. 022 418 27 53
tv@quervane-conseil.ch
www.quervane-conseil.ch
Rue des Verniquets 14
1201 Genève

```html
<!DOCTYPE html>
<html lang="fr">
<head>
<meta charset="utf-8">
<title>Quervane Conseil et Finance SA – cartes de visite</title>
<link rel="stylesheet" href="https://fonts.googleapis.com/css2?family=Open+Sans:wght@400;600;700;800&display=swap">
<style>
  :root {
    --stage: #2b2b2d;
    --paper: #ffffff;
    --paper-shade: #eceef0;
    --blue: #2aa3d8;
    --blue-deep: #1f6fae;
    --ink: #2a2d33;
    --ink-soft: #4a4e56;
    --rule: #b9bec6;
    --band-dark: #33363c;
  }
  * { box-sizing: border-box; margin: 0; padding: 0; }
  html, body { width: 1200px; height: 997px; overflow: hidden; }
  body {
    background: var(--stage);
    font-family: "Open Sans", Arial, sans-serif;
    display: flex;
    flex-direction: column;
    align-items: center;
    justify-content: space-evenly;
  }
  .card {
    position: relative;
    width: 680px;
    height: 440px;
    background: linear-gradient(135deg, var(--paper) 40%, var(--paper-shade) 100%);
    overflow: hidden;
    box-shadow: 0 14px 30px rgba(0,0,0,.45);
  }
  .card__art { position: absolute; inset: 0; width: 100%; height: 100%; }
  .brand {
    position: absolute;
    left: 40px;
    top: 206px;
    display: flex;
    align-items: center;
    gap: 12px;
  }
  .brand__mark { width: 30px; height: 30px; background: var(--blue-deep); }
  .brand__name {
    font-size: 34px;
    font-weight: 700;
    letter-spacing: 1.5px;
    color: var(--ink-soft);
    line-height: 1;
  }
  .details {
    position: absolute;
    left: 352px;
    top: 112px;
    width: 320px;
    color: var(--ink);
  }
  .details__name { font-size: 17px; font-weight: 700; color: var(--blue); line-height: 1.2; }
  .details__role {
    font-size: 13px; font-weight: 600; line-height: 1.35;
    padding-bottom: 3px; border-bottom: 1px solid var(--rule);
    display: inline-block;
  }
  .details__company { margin-top: 14px; font-size: 14.5px; font-weight: 700; color: var(--blue); }
  .details__address { font-size: 13.5px; line-height: 1.35; }
  .details__rule { width: 40px; height: 2px; background: var(--blue); margin: 4px 0 16px; }
  .contact { list-style: none; font-size: 14px; }
  .contact li { display: flex; align-items: center; gap: 8px; margin-bottom: 5px; }
  .contact svg { width: 18px; height: 18px; flex: none; }
  .services {
    position: absolute;
    right: 18px;
    bottom: 30px;
    font-size: 10.5px;
    font-weight: 600;
    letter-spacing: .3px;
    text-transform: uppercase;
    color: var(--ink);
  }
  .services i { font-style: normal; color: var(--blue); }
  .website {
    position: absolute;
    left: 28px;
    bottom: 15px;
    font-size: 17px;
    font-weight: 700;
    letter-spacing: 2px;
    color: var(--paper);
  }
</style>
</head>
<body>

<svg width="0" height="0" style="position:absolute" aria-hidden="true">
  <defs>
    <linearGradient id="divider-fade" x1="0" y1="0" x2="0" y2="1">
      <stop offset="0" stop-color="#2aa3d8" stop-opacity="0"/>
      <stop offset=".5" stop-color="#2aa3d8"/>
      <stop offset="1" stop-color="#2aa3d8" stop-opacity="0"/>
    </linearGradient>
    <symbol id="icon-phone" viewBox="0 0 18 18">
      <circle cx="9" cy="9" r="9" fill="#2aa3d8"/>
      <path d="M5 7.5c0-1.2 1.8-2 4-2s4 .8 4 2l-1.3.4-.4-1.1c-.8-.3-3.8-.3-4.6 0l-.4 1.1zM6 8.5h6l.8 4H5.2z" fill="#fff"/>
    </symbol>
    <symbol id="icon-mail" viewBox="0 0 18 18">
      <circle cx="9" cy="9" r="9" fill="#2aa3d8"/>
      <rect x="4.5" y="6" width="9" height="6.5" fill="#fff"/>
      <path d="M4.5 6l4.5 3.6L13.5 6" fill="none" stroke="#2aa3d8" stroke-width="1"/>
    </symbol>
  </defs>
</svg>

<section class="card card--en" lang="en">
  <svg class="card__art" viewBox="0 0 680 440" aria-hidden="true">
    <line x1="332" y1="110" x2="312" y2="278" stroke="url(#divider-fade)" stroke-width="2"/>
    <polygon points="320,418 680,418 680,440 330,440" fill="var(--band-dark)"/>
    <polygon points="0,392 320,392 350,440 0,440" fill="var(--blue)"/>
  </svg>
  <div class="brand">
    <span class="brand__mark"></span>
    <span class="brand__name">QUERVANE</span>
  </div>
  <div class="details">
    <p class="details__name">Tomas de Valbueno</p>
    <p class="details__role">Director/Founder Certified Accountant</p>
    <p class="details__company">Quervane Advisory &amp; Finance SA</p>
    <p class="details__address">Rue des Verniquets 14<br>1201 Genève</p>
    <div class="details__rule"></div>
    <ul class="contact">
      <li><svg><use href="#icon-phone"/></svg>022 418 27 53</li>
      <li><svg><use href="#icon-mail"/></svg>tv@quervane-conseil.ch</li>
    </ul>
  </div>
  <p class="services"><i>●</i>Accounting, <i>●</i>Tax, <i>●</i>Audit &amp; <i>●</i>Financial Management</p>
  <p class="website">www.quervane-conseil.ch</p>
</section>

<section class="card card--fr">
  <svg class="card__art" viewBox="0 0 680 440" aria-hidden="true">
    <line x1="332" y1="110" x2="312" y2="278" stroke="url(#divider-fade)" stroke-width="2"/>
    <polygon points="320,418 680,418 680,440 330,440" fill="var(--band-dark)"/>
    <polygon points="0,392 320,392 350,440 0,440" fill="var(--blue)"/>
  </svg>
  <div class="brand">
    <span class="brand__mark"></span>
    <span class="brand__name">QUERVANE</span>
  </div>
  <div class="details">
    <p class="details__name">Tomas de Valbueno</p>
    <p class="details__role">Directeur et Fondateur Expert-comptable diplômé</p>
    <p class="details__company">Quervane Advisory &amp; Finance SA</p>
    <p class="details__address">Rue des Verniquets 14<br>1201 Genève</p>
    <div class="details__rule"></div>
    <ul class="contact">
      <li><svg><use href="#icon-phone"/></svg>022 418 27 53</li>
      <li><svg><use href="#icon-mail"/></svg>tv@quervane-conseil.ch</li>
    </ul>
  </div>
  <p class="services"><i>●</i>Accounting, <i>●</i>Tax, <i>●</i>Audit &amp; <i>●</i>Financial Management</p>
  <p class="website">www.quervane-conseil.ch</p>
</section>

</body>
</html>
```